Flyer design for webdesign company

create a flyer that can be printed or sent as an email. The flyer needs to be professional, modern and engaging.

Reason: opportunity for all designers to get their designs in.

Target Market(s)

business owners that do not have a website

Industry/Entity Type

It Company

Font styles to use
Sans Serif

```html
<!DOCTYPE html>
<html lang="en">
<head>
<meta charset="utf-8">
<title>Dry Cleaning Websites Flyer</title>
<link rel="stylesheet" href="https://fonts.googleapis.com/css2?family=Montserrat:ital,wght@0,300;0,400;0,600;0,700;1,400&family=Pacifico&display=swap">
<style>
  :root {
    --orange: #f18a21;
    --charcoal: #3f3f41;
    --charcoal-dark: #353537;
    --white: #ffffff;
    --text-dark: #333335;
    --photo-top: #b9bcb2;
    --photo-mid: #8a8f7c;
    --photo-low: #5d6052;
    --studio-light: #e4e3e0;
    --studio-dark: #c4c2be;
  }
  * { margin: 0; padding: 0; box-sizing: border-box; }
  html, body { width: 858px; height: 1200px; overflow: hidden; background: var(--white); }
  body { font-family: "Montserrat", Arial, sans-serif; }
  .flyer { position: relative; width: 858px; height: 1200px; overflow: hidden; }

  .hero-photo {
    position: absolute; left: 0; top: 0; width: 858px; height: 670px;
    background: linear-gradient(180deg, var(--photo-top) 0%, var(--photo-mid) 50%, var(--photo-low) 100%);
  }
  .hero-shade {
    position: absolute; left: 0; top: 240px; width: 858px; height: 430px;
    background: linear-gradient(180deg, rgba(0,0,0,0) 0%, rgba(0,0,0,0.3) 40%, rgba(0,0,0,0.4) 100%);
  }
  .hero-copy { position: absolute; left: 0; top: 280px; width: 858px; text-align: center; color: var(--white); }
  .hero-kicker { font-size: 38px; font-weight: 300; letter-spacing: 0.5px; line-height: 48px; }
  .hero-kicker strong { font-weight: 700; }
  .hero-script { font-family: "Pacifico", cursive; color: var(--orange); font-size: 50px; line-height: 58px; margin-top: -8px; }
  .hero-rule { width: 76px; height: 4px; background: var(--white); margin: 8px auto 14px; }
  .hero-product { font-size: 33px; font-weight: 700; color: var(--orange); line-height: 42px; }
  .hero-sub { font-size: 33px; font-weight: 300; line-height: 44px; }

  .offer-band {
    position: absolute; left: 0; top: 575px; width: 858px; height: 95px; background: var(--orange); color: var(--white);
  }
  .offer-lead { position: absolute; left: 214px; top: 21px; font-size: 19px; font-weight: 400; white-space: nowrap; }
  .offer-lead em { font-style: italic; }
  .offer-alert { position: absolute; left: 214px; top: 52px; font-size: 17.5px; font-weight: 700; white-space: nowrap; }

  .price-badge { position: absolute; left: 12px; top: 512px; width: 190px; height: 190px; }

  .benefits {
    position: absolute; left: 0; top: 670px; width: 858px; height: 215px; background: var(--charcoal);
    display: flex;
  }
  .benefit { flex: 1; position: relative; text-align: center; color: var(--white); padding-top: 20px; }
  .benefit + .benefit::before {
    content: ""; position: absolute; left: 0; top: 22px; height: 170px; width: 1px; background: rgba(255,255,255,0.55);
  }
  .benefit-icon { width: 84px; height: 84px; margin: 0 auto; display: block; }
  .benefit-text { font-size: 18px; font-weight: 300; line-height: 22px; margin-top: 20px; }
  .benefit-note { font-size: 14px; }

  .contact { position: absolute; left: 0; top: 885px; width: 858px; height: 198px; background: var(--white); }
  .brand { position: absolute; left: 60px; top: 40px; width: 150px; text-align: center; }
  .brand-dot { width: 62px; height: 62px; border-radius: 50%; background: var(--orange); margin: 0 auto 14px; }
  .brand-name { font-size: 16px; font-weight: 600; color: var(--orange); }
  .contact-copy { position: absolute; left: 232px; top: 20px; color: var(--text-dark); }
  .price { font-size: 27px; font-weight: 400; line-height: 32px; }
  .price strong { color: var(--orange); font-weight: 700; }
  .price-note { font-size: 19px; font-weight: 700; color: var(--orange); line-height: 26px; }
  .pitch { font-size: 18.5px; font-weight: 400; line-height: 24px; margin-top: 6px; }
  .contact-line { font-size: 19px; font-weight: 700; color: var(--orange); line-height: 25px; }
  .staff-photo {
    position: absolute; left: 596px; top: 0; width: 262px; height: 198px;
    background: linear-gradient(90deg, var(--studio-light) 0%, var(--studio-dark) 100%);
  }

  .closing {
    position: absolute; left: 0; top: 1083px; width: 858px; height: 117px; background: var(--charcoal-dark);
    text-align: center; color: var(--white);
  }
  .closing-note { font-size: 19px; font-weight: 400; margin-top: 20px; letter-spacing: 0.3px; }
  .closing-script { font-family: "Pacifico", cursive; color: var(--orange); font-size: 29px; line-height: 44px; }
</style>
</head>
<body>
<div class="flyer">
  <div class="hero-photo" role="img" aria-label="Photo of a smiling woman outdoors carrying a garment over her shoulder, trees and city buildings behind"></div>
  <div class="hero-shade"></div>
  <div class="hero-copy">
    <p class="hero-kicker">ATTRACT MORE <strong>CUSTOMERS</strong></p>
    <p class="hero-script">Make More Money</p>
    <div class="hero-rule"></div>
    <p class="hero-product">DRY CLEANING WEBSITES</p>
    <p class="hero-sub">FOR YOUR BUSINESS</p>
  </div>

  <div class="offer-band">
    <p class="offer-lead"><em>Beat your competition with</em> better visibility and credibility</p>
    <p class="offer-alert">YOU'RE LOSING MANY CUSTOMERS BY NOT HAVING A WEBSITE</p>
  </div>

  <svg class="price-badge" viewBox="0 0 150 150" aria-label="Websites for only $3 a day">
    <defs>
      <path id="badgeArc" d="M 14 82 A 61 61 0 0 1 136 82"/>
      <clipPath id="badgeInner"><circle cx="75" cy="82" r="46"/></clipPath>
    </defs>
    <circle cx="75" cy="82" r="56" fill="#ffffff"/>
    <g clip-path="url(#badgeInner)">
      <rect x="0" y="0" width="150" height="150" fill="#3f3f41"/>
      <polygon points="0,0 150,0 150,80 0,100" fill="#f18a21"/>
    </g>
    <circle cx="75" cy="82" r="46" fill="none" stroke="#ffffff" stroke-width="2" stroke-dasharray="3 3"/>
    <text font-family="Montserrat, sans-serif" font-size="15" font-weight="600" fill="#ffffff" letter-spacing="1">
      <textPath href="#badgeArc" startOffset="50%" text-anchor="middle">websites for only</textPath>
    </text>
    <text x="75" y="84" text-anchor="middle" font-family="Montserrat, sans-serif" font-size="30" font-weight="700" fill="#ffffff">$3</text>
    <text x="75" y="114" text-anchor="middle" font-family="Pacifico, cursive" font-size="20" fill="#ffffff">a day</text>
  </svg>

  <div class="benefits">
    <div class="benefit">
      <svg class="benefit-icon" viewBox="0 0 84 84" aria-hidden="true">
        <circle cx="42" cy="42" r="33" fill="none" stroke="#ffffff" stroke-width="9"/>
        <circle cx="42" cy="42" r="33" fill="none" stroke="#f18a21" stroke-width="9" stroke-dasharray="201 207" transform="rotate(-90 42 42)"/>
        <text x="42" y="49" text-anchor="middle" font-family="Montserrat, sans-serif" font-size="19" font-weight="700" fill="#ffffff">97%</text>
      </svg>
      <p class="benefit-text">97% of people<br>look online for<br>businesses</p>
    </div>
    <div class="benefit">
      <svg class="benefit-icon" viewBox="0 0 84 84" aria-hidden="true">
        <rect x="10" y="18" width="62" height="42" rx="2" fill="none" stroke="#ffffff" stroke-width="3"/>
        <rect x="36" y="60" width="10" height="8" fill="#ffffff"/>
        <rect x="26" y="68" width="30" height="3" fill="#ffffff"/>
        <path d="M 30 50 L 60 14 L 66 19 L 36 55 Z" fill="#f18a21"/>
        <path d="M 30 50 L 27 58 L 36 55 Z" fill="#ffffff"/>
      </svg>
      <p class="benefit-text">BEAUTIFUL<br>WEBSITES<br>AVAILABLE NOW</p>
    </div>
    <div class="benefit">
      <svg class="benefit-icon" viewBox="0 0 84 84" aria-hidden="true">
        <circle cx="42" cy="42" r="36" fill="none" stroke="#ffffff" stroke-width="3"/>
        <text x="42" y="56" text-anchor="middle" font-family="Montserrat, sans-serif" font-size="40" font-weight="400" fill="#f18a21">$</text>
      </svg>
      <p class="benefit-text">Affordable<br>websites to fit<br>your budget</p>
    </div>
    <div class="benefit">
      <svg class="benefit-icon" viewBox="0 0 84 84" aria-hidden="true">
        <circle cx="30" cy="32" r="16" fill="#f18a21"/>
        <circle cx="52" cy="50" r="20" fill="#ffffff"/>
      </svg>
      <p class="benefit-text">Social Media<br>setup options<br><span class="benefit-note">(Connectly &amp; Friendbook)</span></p>
    </div>
  </div>

  <div class="contact">
    <div class="brand">
      <div class="brand-dot"></div>
      <p class="brand-name">nimbuswebsites</p>
    </div>
    <div class="contact-copy">
      <p class="price">ONLY <strong>$99/MONTH</strong></p>
      <p class="price-note">That's just $3/day for your website</p>
      <p class="pitch">Stop wasting money on<br>mailers and print advertising.</p>
      <p class="contact-line">1-800-555-0142</p>
      <p class="contact-line">www.nimbus-websites.com</p>
    </div>
    <div class="staff-photo" role="img" aria-label="Photo of a smiling dry cleaning worker holding a garment in front of a clothing rack"></div>
  </div>

  <div class="closing">
    <p class="closing-note">LIMITED TO ONLY 4 WEBSITES PER AREA.</p>
    <p class="closing-script">Don't miss out!</p>
  </div>
</div>
</body>
</html>
```